Grace Fellowship Ardmore, MS needs a Business Card design

We are in the process of rebranding our church with a new logo with a fresh appeal to younger families moving into our community and joining our church. We are in need of a new business card design and would like to see 2 sided designs that incorporate the web color 00cccc.

We would like to have our logo, church name (grace fellowship ardmore) and our what we are about (gather.grow.serve.) in addition to the following information:
Name: Dr. Samuel Whitfield
Title: Teaching Pastor
Phone: 6015550142
Email: swhitfield@gfcardmore.example
Website: www.gfcardmore.example
Address: 714 N Elmwood Avenue Brandon, MS 39187

Target Market(s)

Brandon, MS is a bedroom community outside of Jackson that is experiencing exponential growth with young professionals/young families moving in. We are making a lot of changes to reach this demographic while still honoring and continuing to reach those who have lived here for a while.

Industry/Entity Type

Church

Contact Information for Business Card

Grace Fellowship Ardmore - gather.grow.serve.
Dr. Samuel Whitfield
Teaching Pastor
6015550142
swhitfield@gfcardmore.example
www.gfcardmore.example
714 N Elmwood Avenue
Brandon, MS 39187

Font styles to use
Sans Serif

```html
<!DOCTYPE html>
<html lang="en">
<head>
<meta charset="utf-8">
<title>Grace Fellowship Ardmore – Business Card</title>
<link rel="stylesheet" href="https://fonts.googleapis.com/css2?family=Lato:wght@300;400;700&display=swap">
<style>
  :root {
    --bg: #2b2e33;
    --card: #1f1f20;
    --teal: #1fb5a8;
    --teal-light: #00cccc;
    --white: #f2f2f2;
    --muted: #8a8a8a;
    --text: #d8d8d8;
  }
  * { margin: 0; padding: 0; box-sizing: border-box; }
  html, body { width: 1200px; height: 900px; overflow: hidden; }
  body {
    background: var(--bg);
    font-family: "Lato", sans-serif;
    position: relative;
  }
  .card {
    position: absolute;
    left: 310px;
    width: 580px;
    height: 331px;
    background: var(--card);
    border-radius: 24px;
    overflow: hidden;
    box-shadow: 0 12px 30px rgba(0,0,0,.45);
  }
  .card--back { top: 70px; }
  .card--front { top: 490px; }
  .accent-band {
    position: absolute;
    left: 0; bottom: 0;
    width: 100%; height: 40px;
  }
  /* back */
  .back-brand {
    position: absolute;
    left: 0; right: 0; top: 110px;
    display: flex; flex-direction: column; align-items: center; gap: 14px;
  }
  .brand-dot {
    width: 78px; height: 78px; border-radius: 50%;
    background: linear-gradient(120deg, var(--teal) 0%, #e9f5f4 100%);
  }
  .brand-name {
    font-weight: 300;
    font-size: 13px;
    letter-spacing: 1px;
    text-transform: uppercase;
    color: var(--muted);
    white-space: nowrap;
  }
  /* front */
  .front-brand {
    position: absolute;
    left: 50px; top: 40px;
    display: flex; flex-direction: column; align-items: center; gap: 12px;
  }
  .front-brand .brand-dot { width: 82px; height: 82px; }
  .front-brand .brand-name { font-size: 11px; }
  .person {
    position: absolute;
    left: 262px; top: 58px;
  }
  .person-name {
    font-weight: 700;
    font-size: 27px;
    color: var(--white);
    letter-spacing: .2px;
    white-space: nowrap;
  }
  .person-title {
    font-size: 16px;
    color: var(--teal);
    margin-top: 4px;
  }
  .person-address {
    font-size: 13px;
    color: var(--text);
    line-height: 1.4;
    margin-top: 6px;
  }
  .divider {
    position: absolute;
    left: 210px; right: 26px; top: 182px;
    height: 1px;
    background: var(--teal);
  }
  .contact-list {
    position: absolute;
    left: 196px; top: 200px;
    list-style: none;
    display: flex; flex-direction: column; gap: 7px;
  }
  .contact-item {
    display: flex; align-items: center; gap: 12px;
    font-size: 14px;
    color: var(--text);
  }
  .contact-item svg { width: 18px; height: 18px; flex: none; }
  .contact-item .highlight { color: var(--teal); }
</style>
</head>
<body>

<section class="card card--back" aria-label="Card back">
  <div class="back-brand">
    <span class="brand-dot"></span>
    <span class="brand-name">Grace Fellowship Ardmore</span>
  </div>
  <svg class="accent-band" viewBox="0 0 580 40" preserveAspectRatio="none" aria-hidden="true">
    <path d="M0 8 H70 Q82 8 86 20 Q90 30 104 30 H476 Q490 30 494 20 Q498 8 510 8 H580 V40 H0 Z" fill="var(--teal)"/>
  </svg>
</section>

<section class="card card--front" aria-label="Card front">
  <div class="front-brand">
    <span class="brand-dot"></span>
    <span class="brand-name">Grace Fellowship Ardmore</span>
  </div>

  <div class="person">
    <h1 class="person-name">Dr. Samuel Whitfield</h1>
    <p class="person-title">Teaching Pastor</p>
    <p class="person-address">714 N Elmwood Avenue<br>Ardmore, MS 39187</p>
  </div>

  <div class="divider"></div>

  <ul class="contact-list">
    <li class="contact-item">
      <svg viewBox="0 0 18 18" aria-hidden="true"><rect x="5" y="1.5" width="8" height="15" rx="1.5" fill="none" stroke="var(--teal)" stroke-width="1.5"/><line x1="8" y1="14" x2="10" y2="14" stroke="var(--teal)" stroke-width="1.5"/></svg>
      <span>6015550142</span>
    </li>
    <li class="contact-item">
      <svg viewBox="0 0 18 18" aria-hidden="true"><circle cx="9" cy="9" r="3" fill="none" stroke="var(--teal)" stroke-width="1.6"/><path d="M12 7 V10.5 Q12 12.5 14 12.5 Q16 12.5 16 9 A7 7 0 1 0 12 15.3" fill="none" stroke="var(--teal)" stroke-width="1.6"/></svg>
      <span>swhitfield@gfcardmore.example</span>
    </li>
    <li class="contact-item">
      <svg viewBox="0 0 18 18" aria-hidden="true"><circle cx="9" cy="9" r="7" fill="none" stroke="var(--teal)" stroke-width="1.4"/><ellipse cx="9" cy="9" rx="3" ry="7" fill="none" stroke="var(--teal)" stroke-width="1.2"/><line x1="2" y1="9" x2="16" y2="9" stroke="var(--teal)" stroke-width="1.2"/></svg>
      <span>www.<span class="highlight">gfcardmore</span>.example</span>
    </li>
  </ul>

  <svg class="accent-band" viewBox="0 0 580 40" preserveAspectRatio="none" aria-hidden="true">
    <path d="M0 8 H70 Q82 8 86 20 Q90 30 104 30 H476 Q490 30 494 20 Q498 8 510 8 H580 V40 H0 Z" fill="var(--teal)"/>
  </svg>
</section>

</body>
</html>
```